Business card with professional look

I would like a creative yet professional looking business card for our business. We sell broadcast TV related security products for mobile phones, set top boxes, and tablets. Our customers are international. We have a logo we like and I would like to possibly add some color to the business card but keep it professional looking.

Target Market(s)

Professionals in the TV, cable, ans Satellite industries

Industry/Entity Type

Cable Tv

Contact Information for Business Card

Name Ned Vastermill, title CEO, Address 8130 Harborline Court, Suite 400, Del Arvo, CA 91584 USA, phone numbers m:+1.619.284.7302 o:+1.855.672.9140, email, logo

Font styles to use
Other font styles liked:
• Open to any font that looks good with logo

Requirements
Must have
• professional look with colors coordinated with logo colors. would like to add one or two different colors as well as some form of background color

```html
<!DOCTYPE html>
<html lang="en">
<head>
<meta charset="utf-8">
<title>Vantiro – Business Card</title>
<link rel="stylesheet" href="https://fonts.googleapis.com/css2?family=Quicksand:wght@500;600;700&display=swap">
<style>
  :root {
    --stage: #4a4a4a;
    --paper: #ffffff;
    --panel: #2a2b2d;
    --panel-soft: #34363a;
    --brand-blue: #1f8fd6;
    --brand-blue-deep: #1468a8;
    --brand-blue-fold: #0e4f80;
    --ink: #3d3f42;
    --light: #ffffff;
  }
  html, body {
    margin: 0;
    width: 1200px;
    height: 792px;
    overflow: hidden;
    background: var(--stage);
    font-family: "Quicksand", sans-serif;
  }
  .card {
    position: absolute;
    left: 110px;
    top: 116px;
    width: 980px;
    height: 560px;
    background: var(--paper);
    overflow: hidden;
    box-shadow: 0 20px 50px rgba(0,0,0,.35);
  }
  .brand-side {
    position: absolute;
    left: 0; top: 0;
    width: 460px; height: 560px;
    background: var(--paper);
  }
  .brand-mark {
    position: absolute;
    left: 90px; top: 180px;
    display: flex; align-items: center; gap: 16px;
  }
  .brand-dot {
    width: 34px; height: 34px;
    border-radius: 50%;
    background: var(--brand-blue);
  }
  .brand-name {
    font-weight: 700;
    font-size: 64px;
    color: var(--ink);
    letter-spacing: -1px;
  }
  .contact-side {
    position: absolute;
    left: 460px; top: 0;
    width: 520px; height: 560px;
    background: var(--panel);
  }
  .world-backdrop {
    position: absolute;
    inset: 0;
    background: radial-gradient(ellipse at 55% 45%, var(--panel-soft) 0%, var(--panel) 70%);
  }
  .ribbon {
    position: absolute;
    left: 440px;
    width: 540px;
    background: linear-gradient(90deg, var(--brand-blue) 0%, var(--brand-blue-deep) 100%);
  }
  .ribbon-fold {
    position: absolute;
    left: 0; bottom: -16px;
    width: 0; height: 0;
    border-top: 16px solid var(--brand-blue-fold);
    border-left: 20px solid transparent;
  }
  .ribbon-name { top: 88px; height: 84px; }
  .ribbon-address { top: 372px; height: 112px; }
  .tag {
    position: absolute;
    width: 46px; height: 62px;
  }
  .tag svg { display: block; }
  .tag-name { left: 52px; top: 10px; }
  .tag-address { left: 52px; top: 24px; }
  .tag-phone { left: 520px; top: 214px; }
  .tag-email { left: 540px; top: 300px; }
  .person-name {
    position: absolute;
    left: 120px; top: 12px;
    margin: 0;
    color: var(--light);
    font-weight: 700;
    font-size: 34px;
    line-height: 1.1;
  }
  .person-title {
    position: absolute;
    left: 122px; top: 50px;
    margin: 0;
    color: var(--light);
    font-weight: 700;
    font-size: 20px;
  }
  .contact-line {
    position: absolute;
    margin: 0;
    color: var(--light);
    font-weight: 500;
    font-size: 22px;
    line-height: 1.3;
  }
  .phones { left: 594px; top: 205px; }
  .email { left: 614px; top: 312px; }
  .address {
    left: 120px; top: 14px;
    font-size: 23px;
    line-height: 1.22;
  }
</style>
</head>
<body>
  <div class="card">
    <section class="brand-side">
      <div class="brand-mark">
        <span class="brand-dot"></span>
        <span class="brand-name">Vantiro</span>
      </div>
    </section>

    <section class="contact-side">
      <div class="world-backdrop" role="img" aria-label="Faint world map texture behind the contact details"></div>
    </section>

    <div class="ribbon ribbon-name">
      <span class="ribbon-fold"></span>
      <div class="tag tag-name">
        <svg width="46" height="62" viewBox="0 0 46 62">
          <path d="M0 0H46V50L23 62L0 50Z" fill="#fff"/>
          <circle cx="23" cy="20" r="6" fill="#1f8fd6"/>
          <path d="M12 40c0-8 5-12 11-12s11 4 11 12Z" fill="#1f8fd6"/>
        </svg>
      </div>
      <p class="person-name">Ned Vastermill</p>
      <p class="person-title">CEO</p>
    </div>

    <div class="tag tag-phone">
      <svg width="46" height="62" viewBox="0 0 46 62">
        <path d="M0 0H46V50L23 62L0 50Z" fill="#1f8fd6"/>
        <path d="M15 14c2-2 4-1 5 1l2 4c1 2 0 3-1 4l-1 1c1 3 4 6 7 7l1-1c1-1 2-2 4-1l4 2c2 1 3 3 1 5l-2 2c-6 3-22-13-20-21Z" fill="#fff"/>
      </svg>
    </div>
    <p class="contact-line phones">m:+1.619.284.7302<br>o:+1.855.672.9140</p>

    <div class="tag tag-email">
      <svg width="46" height="62" viewBox="0 0 46 62">
        <path d="M0 0H46V50L23 62L0 50Z" fill="#1f8fd6"/>
        <circle cx="23" cy="25" r="11" fill="none" stroke="#fff" stroke-width="3"/>
        <path d="M12 25H34M23 14c-5 6-5 16 0 22M23 14c5 6 5 16 0 22" fill="none" stroke="#fff" stroke-width="2"/>
      </svg>
    </div>
    <p class="contact-line email">info@vantiro.com</p>

    <div class="ribbon ribbon-address">
      <span class="ribbon-fold"></span>
      <div class="tag tag-address">
        <svg width="46" height="62" viewBox="0 0 46 62">
          <path d="M0 0H46V50L23 62L0 50Z" fill="#fff"/>
          <path d="M23 10c-7 0-11 5-11 11 0 8 11 19 11 19s11-11 11-19c0-6-4-11-11-11Z" fill="#1f8fd6"/>
          <circle cx="23" cy="21" r="4" fill="#fff"/>
        </svg>
      </div>
      <p class="contact-line address">8130 Harborline Court,<br>Suite 400, Del Arvo,<br>CA 91584 USA</p>
    </div>
  </div>
</body>
</html>
```